Bref créative
Trucking Company Business Cards Stationary
KVR Freight Solutions
Professional
Beto Quiroga
Terminal Manager
4100 Harborview Blvd
La Porte, TX 77571
kvrfreightsolutions@mailbox-example.com
i would like something similar to this on the back side of card
i would also like something similar to this on the back side of my card

```html
<!DOCTYPE html>
<html lang="en">
<head>
<meta charset="utf-8">
<title>KVR Freight Solutions – Business Card</title>
<link rel="stylesheet" href="https://fonts.googleapis.com/css2?family=Open+Sans:wght@400;600;700;800&display=swap">
<style>
  :root {
    --brand-red: #c4161c;
    --deep-red: #8f0f13;
    --ink: #4a4a4a;
    --soft-ink: #6d6d6d;
    --card: #ffffff;
    --backdrop: #e9e7e4;
  }
  * { margin: 0; padding: 0; box-sizing: border-box; }
  html, body { width: 1200px; height: 629px; overflow: hidden; }
  body {
    background: var(--backdrop);
    font-family: "Open Sans", Arial, sans-serif;
    color: var(--ink);
    position: relative;
  }
  .card {
    position: absolute;
    top: 164px;
    width: 525px;
    height: 300px;
    background: var(--card);
    box-shadow: 0 6px 18px rgba(0,0,0,0.12);
    overflow: hidden;
  }
  .card--back { left: 50px; }
  .card--front { left: 625px; }

  /* Back side */
  .card--back .brand-lockup {
    position: absolute;
    inset: 0;
    display: flex;
    align-items: center;
    justify-content: center;
    gap: 12px;
  }
  .brand-mark {
    width: 22px; height: 22px;
    background: var(--brand-red);
  }
  .brand-name {
    font-weight: 800;
    color: var(--brand-red);
    font-size: 30px;
    letter-spacing: 0.5px;
  }

  /* Front side */
  .card--front .brand-lockup {
    position: absolute;
    left: 30px; top: 40px;
    display: flex; align-items: center; gap: 8px;
  }
  .card--front .brand-mark { width: 14px; height: 14px; }
  .card--front .brand-name { font-size: 18px; }

  .holder {
    position: absolute;
    right: 34px; top: 108px;
    text-align: left;
  }
  .holder-name {
    font-weight: 700;
    color: var(--brand-red);
    font-size: 17px;
  }
  .holder-title {
    font-size: 13px;
    color: var(--soft-ink);
    margin-top: 2px;
  }

  .contact-list {
    position: absolute;
    left: 30px; top: 170px;
    list-style: none;
    font-size: 10.5px;
    line-height: 1.75;
    color: var(--ink);
  }
  .contact-list li { display: flex; align-items: center; gap: 8px; }
  .contact-icon { width: 11px; height: 11px; flex: none; }

  .accent-band {
    position: absolute;
    left: 0; right: 0; bottom: 0;
    height: 12px;
    background: linear-gradient(90deg, var(--deep-red), var(--brand-red));
  }
</style>
</head>
<body>
  <section class="card card--back" aria-label="Card back">
    <div class="brand-lockup">
      <span class="brand-mark"></span>
      <span class="brand-name">KVR Freight Solutions</span>
    </div>
  </section>

  <section class="card card--front" aria-label="Card front">
    <div class="brand-lockup">
      <span class="brand-mark"></span>
      <span class="brand-name">KVR Freight Solutions</span>
    </div>

    <div class="holder">
      <p class="holder-name">Beto Quiroga</p>
      <p class="holder-title">Terminal Manager</p>
    </div>

    <ul class="contact-list">
      <li>
        <svg class="contact-icon" viewBox="0 0 12 12"><circle cx="6" cy="6" r="6" fill="#c4161c"/><path d="M6 2.6a2.2 2.2 0 0 0-2.2 2.2C3.8 6.6 6 9.4 6 9.4s2.2-2.8 2.2-4.6A2.2 2.2 0 0 0 6 2.6z" fill="#fff"/></svg>
        <span>4100 Harborview Blvd<br>La Porte, TX 77571</span>
      </li>
      <li>
        <svg class="contact-icon" viewBox="0 0 12 12"><circle cx="6" cy="6" r="6" fill="#c4161c"/><path d="M4 3l1.2 1.6-.6.8c.5.9 1.1 1.5 2 2l.8-.6L9 8l-.8 1C6 9 3 6 3 3.8z" fill="#fff"/></svg>
        <span>(281) 555-0137</span>
      </li>
      <li>
        <svg class="contact-icon" viewBox="0 0 12 12"><circle cx="6" cy="6" r="6" fill="#c4161c"/><rect x="4" y="2.6" width="4" height="6.8" rx="0.8" fill="#fff"/></svg>
        <span>(281) 555-0194</span>
      </li>
      <li>
        <svg class="contact-icon" viewBox="0 0 12 12"><circle cx="6" cy="6" r="6" fill="#c4161c"/><rect x="3" y="4" width="6" height="4.2" fill="#fff"/><path d="M3 4l3 2.3L9 4" stroke="#c4161c" stroke-width="0.7" fill="none"/></svg>
        <span>kvrfreightsolutions@mailbox-example.com</span>
      </li>
      <li>
        <svg class="contact-icon" viewBox="0 0 12 12"><circle cx="6" cy="6" r="6" fill="#c4161c"/><circle cx="6" cy="6" r="3" stroke="#fff" stroke-width="0.8" fill="none"/><path d="M3 6h6M6 3v6" stroke="#fff" stroke-width="0.7"/></svg>
        <span>www.kvrfreight-example.com</span>
      </li>
    </ul>

    <div class="accent-band"></div>
  </section>
</body>
</html>
```